Business Card Design Project

Doctor, Pain Management. Need a new business card design with appointment info on the back. New address is 18 Whitcombe Road, Suite 305, Linwood Park, NJ 07748. Right now I believe the rest of the information is staying the same.

```html
<!DOCTYPE html>
<html lang="en">
<head>
<meta charset="utf-8">
<title>Halcyon Pain Management – Business Card</title>
<link href="https://fonts.googleapis.com/css2?family=Roboto:wght@400;500;700;900&display=swap" rel="stylesheet">
<style>
  :root{
    --bg:#3b4048;
    --card-black:#0b0b0c;
    --gold:#f2b21c;
    --orange:#e0871f;
    --blue:#4f86d6;
    --sky:#6cb7ec;
    --white:#ffffff;
    --ink:#222;
    --ring:#5a7fb8;
  }
  *{margin:0;padding:0;box-sizing:border-box}
  html,body{width:1200px;height:900px;overflow:hidden}
  body{background:var(--bg);font-family:"Roboto",Arial,sans-serif;position:relative}

  .card{position:absolute;left:260px;width:680px;height:388px;overflow:hidden;border-radius:4px;box-shadow:0 10px 24px rgba(0,0,0,.45)}
  .card--front{top:36px;background:var(--card-black)}
  .card--back{top:470px;background:var(--white)}

  /* front */
  .brand{position:absolute;left:40px;top:34px}
  .brand__name{font-weight:900;font-size:58px;line-height:1;color:var(--gold);letter-spacing:1px}
  .brand__sub{font-weight:500;font-size:22px;color:var(--blue);letter-spacing:.5px;margin-top:2px}
  .brand__loc{font-size:13px;color:var(--orange);margin-top:2px}

  .person{position:absolute;left:40px;top:176px}
  .person__name{font-weight:700;font-size:22px;color:var(--gold)}
  .person__title{font-size:16px;color:var(--blue);margin-top:2px}
  .contact-list{list-style:none;margin-top:8px}
  .contact-list li{display:flex;align-items:center;gap:7px;font-size:14px;color:var(--orange);line-height:1.35}
  .contact-list svg{width:12px;height:12px;flex:none}

  .divider{position:absolute;left:40px;right:40px;top:290px;height:1px;background:var(--orange)}

  .front-footer{position:absolute;left:40px;right:40px;top:302px;display:flex;justify-content:space-between;color:var(--orange);font-size:16px;line-height:1.4}
  .front-footer address{font-style:normal}
  .phones li{list-style:none;display:flex;align-items:center;gap:6px;justify-content:flex-end}
  .phones svg{width:13px;height:13px}

  .wordmark{position:absolute;display:flex;align-items:center;gap:12px;font-weight:700;color:var(--sky)}
  .card--front .wordmark{right:44px;top:140px;font-size:50px}
  .wordmark__dot{border-radius:50%;background:var(--sky)}
  .card--front .wordmark__dot{width:22px;height:22px}

  /* back */
  .back-top{position:absolute;left:0;top:0;width:680px;height:170px}
  .back-contacts{position:absolute;left:250px;top:12px;list-style:none;color:var(--white);font-size:13px;line-height:1.3}
  .back-contacts li{display:flex;align-items:center;gap:6px}
  .back-contacts svg{width:11px;height:11px;flex:none}
  .card--back .wordmark{right:24px;top:64px;font-size:32px;gap:9px}
  .card--back .wordmark__dot{width:14px;height:14px}

  .appt-title{position:absolute;left:320px;top:112px;font-size:20px;font-weight:500;color:var(--blue)}
  .form-label{position:absolute;font-size:14px;color:var(--ink)}
  .form-line{position:absolute;height:1px;background:var(--ink)}
  .days{position:absolute;left:30px;top:212px;display:flex;gap:24px;list-style:none;font-size:14px;color:var(--ink)}
  .days li{display:flex;align-items:center;gap:6px}
  .radio{display:inline-block;width:15px;height:15px;border-radius:50%;border:1.5px solid var(--ring);background:linear-gradient(#fff,#e6eef8)}
  .slash{position:absolute;font-size:14px;color:var(--blue)}

  .back-note{position:absolute;left:0;bottom:0;width:100%;height:42px;background:var(--card-black);color:var(--white);font-size:15px;display:flex;align-items:center;padding-left:26px}
  .back-note em{font-style:normal;color:var(--gold)}
</style>
</head>
<body>

<section class="card card--front" aria-label="Business card front">
  <div class="brand">
    <div class="brand__name">HALCYON</div>
    <div class="brand__sub">PAIN MANAGEMENT</div>
    <div class="brand__loc">Location in New Jersey &amp; New York</div>
  </div>

  <div class="person">
    <div class="person__name">Liang Morrow, M.D., Ph.D.</div>
    <div class="person__title">Board Certified Anesthesiologist</div>
    <ul class="contact-list">
      <li><svg viewBox="0 0 12 12"><rect x="0.5" y="2" width="11" height="8" fill="#4f86d6"/><path d="M0.5 2 6 7 11.5 2" fill="none" stroke="#fff" stroke-width="1"/></svg>halcyonpm.office@mailbox.com</li>
      <li><svg viewBox="0 0 12 12"><circle cx="6" cy="6" r="5.2" fill="none" stroke="#4f86d6" stroke-width="1.2"/><path d="M1 6h10M6 1c-2.5 3-2.5 7 0 10M6 1c2.5 3 2.5 7 0 10" fill="none" stroke="#4f86d6" stroke-width="1"/></svg>halcyonpm.com</li>
    </ul>
  </div>

  <div class="wordmark"><span class="wordmark__dot"></span>Halcyon</div>

  <div class="divider"></div>

  <div class="front-footer">
    <address>18 Whitcombe Road, Suite 305<br>Linwood Park, NJ 07748</address>
    <ul class="phones">
      <li>973.555.0148 <svg viewBox="0 0 12 12"><path d="M2.5 1l2 2.2-1 1.3a7 7 0 0 0 4 4l1.3-1 2.2 2-1.3 1.5C5 11 1 7 1 2.3z" fill="#4f86d6"/></svg></li>
      <li>973.555.0162 <svg viewBox="0 0 12 12"><rect x="3" y="1" width="6" height="4" fill="#4f86d6"/><rect x="1" y="5" width="10" height="5" rx="1" fill="#4f86d6"/><rect x="3" y="8" width="6" height="3" fill="#fff"/></svg></li>
    </ul>
  </div>
</section>

<section class="card card--back" aria-label="Business card back, appointment reminder">
  <svg class="back-top" viewBox="0 0 680 170" aria-hidden="true">
    <path d="M0 0H462C484 16 494 42 484 70C474 86 468 92 460 100H0Z" fill="#e0871f"/>
    <path d="M470 0H680V160H478C464 130 472 102 486 74C498 44 490 18 470 0Z" fill="#0b0b0c"/>
    <path d="M462 0H470C490 18 498 44 486 74C474 100 464 130 478 160H472C458 130 466 100 480 72C490 44 482 16 462 0Z" fill="#f2b21c"/>
  </svg>

  <ul class="back-contacts">
    <li><svg viewBox="0 0 12 12"><path d="M2.5 1l2 2.2-1 1.3a7 7 0 0 0 4 4l1.3-1 2.2 2-1.3 1.5C5 11 1 7 1 2.3z" fill="#fff"/></svg>973.555.0148</li>
    <li><svg viewBox="0 0 12 12"><rect x="3" y="1" width="6" height="4" fill="#fff"/><rect x="1" y="5" width="10" height="5" rx="1" fill="#fff"/></svg>973.555.0162</li>
    <li><svg viewBox="0 0 12 12"><rect x="0.5" y="2" width="11" height="8" fill="#fff"/><path d="M0.5 2 6 7 11.5 2" fill="none" stroke="#e0871f" stroke-width="1"/></svg>halcyonpm.office@mailbox.com</li>
    <li><svg viewBox="0 0 12 12"><circle cx="6" cy="6" r="5.2" fill="none" stroke="#fff" stroke-width="1.2"/><path d="M1 6h10" stroke="#fff"/></svg>halcyonpm.com</li>
  </ul>

  <div class="wordmark"><span class="wordmark__dot"></span>Halcyon</div>

  <div class="appt-title">Appointment</div>

  <span class="form-label" style="left:30px;top:164px">For :</span>
  <span class="form-line" style="left:66px;top:180px;width:584px"></span>

  <ul class="days">
    <li>Mon <span class="radio"></span></li>
    <li>Tue <span class="radio"></span></li>
    <li>Wed <span class="radio"></span></li>
    <li>Thu <span class="radio"></span></li>
    <li>Fri <span class="radio"></span></li>
    <li>Sat <span class="radio"></span></li>
    <li>Sun <span class="radio"></span></li>
  </ul>

  <span class="form-label" style="left:30px;top:272px">Date:</span>
  <span class="form-line" style="left:70px;top:288px;width:240px"></span>
  <span class="slash" style="left:145px;top:270px">/</span>
  <span class="slash" style="left:225px;top:270px">/</span>

  <span class="form-label" style="left:350px;top:272px">Time:</span>
  <span class="form-line" style="left:392px;top:288px;width:258px"></span>
  <span class="slash" style="left:505px;top:270px;color:#222">:</span>

  <p class="back-note">If you are&nbsp;<em>unable to keep your appointment</em>, please contact us as soon as possible</p>
</section>

</body>
</html>
```